Badges and fridge magnets (designs needed)

I make and sell badges and fridge magnets.

I'm looking for some new templates to use, preferably funny, quirky, original designs that people might like to display on their fridge etc.

The designs should fit inside a circle. The badge sizes I sell are 25mm, 44mm and 58mm, so the design should be adjustable to those sizes.

To make the badges I need to print them out on A4 paper.

For this order, I would like at least 5 templates.

```html
<!DOCTYPE html>
<html lang="en">
<head>
<meta charset="utf-8">
<title>Quote Badges</title>
<link rel="stylesheet" href="https://fonts.googleapis.com/css2?family=Oswald:wght@500;700&family=Graduate&family=Yesteryear&display=swap">
<style>
  :root {
    --page: #f4efe8;
    --teal: #1f5f59;
    --teal-soft: #7fcfc4;
    --mint: #a8e0d7;
    --sky: #dff2f7;
    --pink: #f3b7c7;
    --pink-deep: #e88aa6;
    --rose: #e0527c;
    --plum: #5a2a3a;
    --white: #ffffff;
  }
  * { margin: 0; padding: 0; box-sizing: border-box; }
  html, body { width: 1200px; height: 998px; overflow: hidden; }
  body { background: var(--page); position: relative; }

  .badge {
    position: absolute;
    width: 330px; height: 330px;
    border-radius: 50%;
    overflow: hidden;
    box-shadow: 0 6px 14px rgba(60, 40, 20, 0.25);
    border: 2px solid rgba(255,255,255,0.7);
  }
  .badge-art { position: absolute; inset: 0; }
  .badge-quote {
    position: absolute; inset: 0;
    display: flex; flex-direction: column; justify-content: center; align-items: center;
    text-align: center;
  }
  .line { display: flex; align-items: baseline; justify-content: center; gap: 6px; white-space: nowrap; }

  .sans { font-family: "Oswald", sans-serif; font-weight: 700; text-transform: uppercase; letter-spacing: 1px; }
  .sans-small { font-family: "Oswald", sans-serif; font-weight: 500; text-transform: uppercase; letter-spacing: 1px; font-size: 18px; line-height: 1.05; }
  .script { font-family: "Yesteryear", cursive; line-height: 0.9; }
  .outlined {
    font-family: "Graduate", serif; color: var(--white); line-height: 1;
    text-shadow: -2px -2px 0 var(--outline), 2px -2px 0 var(--outline), -2px 2px 0 var(--outline), 2px 2px 0 var(--outline),
                 0 2px 0 var(--outline), 0 -2px 0 var(--outline), 2px 0 0 var(--outline), -2px 0 0 var(--outline);
  }

  .badge--happiness { left: 72px; top: 182px; --outline: var(--teal); color: var(--teal); }
  .badge--happiness .badge-art { background: radial-gradient(circle at 50% 40%, #d8f3ee 0%, var(--mint) 45%, var(--teal-soft) 100%); }

  .badge--love { left: 437px; top: 182px; --outline: var(--plum); color: var(--plum); }
  .badge--love .badge-art { background: radial-gradient(circle at 45% 35%, #fde6ec 0%, var(--pink) 50%, var(--pink-deep) 100%); }

  .badge--good { left: 802px; top: 182px; --outline: var(--teal); color: var(--teal); }
  .badge--good .badge-art { background: radial-gradient(circle at 40% 30%, #ffffff 0%, var(--sky) 50%, #a9dcd6 100%); }

  .badge--begin { left: 253px; top: 505px; --outline: var(--plum); color: var(--plum); }
  .badge--begin .badge-art { background: radial-gradient(circle at 55% 45%, #fdeef0 0%, var(--pink) 55%, #e9a0b3 100%); }

  .badge--grateful { left: 625px; top: 505px; --outline: var(--teal); color: var(--teal); }
  .badge--grateful .badge-art { background: radial-gradient(circle at 40% 30%, #fde3ea 0%, var(--pink) 45%, var(--pink-deep) 100%); }
</style>
</head>
<body>

<div class="badge badge--happiness">
  <div class="badge-art" role="img" aria-label="Soft turquoise floral pattern with halftone dots"></div>
  <div class="badge-quote">
    <div class="line"><span class="sans-small" style="align-self:flex-start">Find</span></div>
    <div class="line"><span class="script" style="font-size:58px">Happiness</span><span class="sans-small">in the</span></div>
    <div class="line"><span class="outlined" style="font-size:56px">SIMPLEST</span></div>
    <div class="line"><span class="script" style="font-size:34px">of</span><span class="sans" style="font-size:46px;line-height:1.1">Things</span></div>
  </div>
</div>

<div class="badge badge--love">
  <div class="badge-art" role="img" aria-label="Pink rose floral pattern with halftone dots"></div>
  <div class="badge-quote">
    <div class="line"><span class="sans-small">A simple</span><span class="sans" style="font-size:40px;line-height:1">Act</span></div>
    <div class="line"><span class="sans-small">of</span><span class="script" style="font-size:74px;color:var(--rose)">Love</span><span class="sans-small">can make</span></div>
    <div class="line"><span class="outlined" style="font-size:36px">EXTRAORDINARY</span></div>
    <div class="line"><span class="sans" style="font-size:26px">Things</span><span class="script" style="font-size:46px">Happen</span></div>
  </div>
</div>

<div class="badge badge--good">
  <div class="badge-art" role="img" aria-label="Pale blue and turquoise floral pattern with halftone dots"></div>
  <div class="badge-quote">
    <div class="line"><span class="sans" style="font-size:22px;font-weight:500">No matter</span></div>
    <div class="line"><span class="script" style="font-size:24px">what</span><span class="script" style="font-size:54px">Happens</span></div>
    <div class="line" style="align-items:center"><span class="script" style="font-size:22px">in</span><span class="script" style="font-size:70px">Life</span>
      <span style="display:flex;flex-direction:column;align-items:flex-start"><span class="outlined" style="font-size:38px">BE</span><span class="outlined" style="font-size:40px">GOOD</span></span></div>
    <div class="line"><span class="script" style="font-size:30px">to</span><span class="sans" style="font-size:44px">People</span></div>
  </div>
</div>

<div class="badge badge--begin">
  <div class="badge-art" role="img" aria-label="Pink and sage floral pattern with halftone dots"></div>
  <div class="badge-quote">
    <div class="line" style="align-items:center">
      <span style="display:flex;flex-direction:column;align-items:flex-start"><span class="sans-small">Forget</span><span class="sans" style="font-size:24px;line-height:1.1">Your</span><span class="sans-small">Forgive</span></span>
      <span class="script" style="font-size:68px">Past</span></div>
    <div class="line"><span class="outlined" style="font-size:46px">YOURSELF</span></div>
    <div class="line"><span class="sans-small">&amp; begin</span></div>
    <div class="line"><span class="script" style="font-size:58px">Again</span></div>
  </div>
</div>

<div class="badge badge--grateful">
  <div class="badge-art" role="img" aria-label="Pink rose floral pattern with halftone dots"></div>
  <div class="badge-quote">
    <div class="line"><span class="sans-small" style="font-size:20px">Start each</span></div>
    <div class="line"><span class="script" style="font-size:66px">Day</span><span class="sans-small">with a</span></div>
    <div class="line"><span class="outlined" style="font-size:54px">GRATEFUL</span></div>
    <div class="line"><span class="sans" style="font-size:44px;line-height:1.15">Heart</span></div>
  </div>
</div>

</body>
</html>
```